Brindlewick Pest Control Hotel Brochure

Hi we are looking to get a slick looking brochure designed. It should be 8.5x11, open up to 17x11 and be a total of 4 pages. We are hoping that you guys have something pre-made and ready to go with a quick turn around.
Our target for this one is hotels. The front page should have a hotel of some sort on the front. Inside should say things like "You have pest problems, Brindlewick Pest Control has answers" Maybe some information and statistics that apply to the hotel industry regarding pest control in California/United States.
I have a high resolution logo of ours that I can send over when appropriate.
Our website is www.getbrindlewick.com if you want to see how our company design is.
Hotels

```html
<!DOCTYPE html>
<html lang="en">
<head>
<meta charset="utf-8">
<title>Brindlewick Pest Control – Hotel Brochure</title>
<link rel="stylesheet" href="https://fonts.googleapis.com/css2?family=Poppins:wght@400;500;600;700&family=Montserrat:wght@300;400;500&display=swap">
<style>
:root{
  --blue:#0b66bf;
  --green:#6cc24a;
  --ink:#1d1d1d;
  --grey:#555;
  --paper:#f7f7f7;
  --white:#ffffff;
  --stage:#7c7c7c;
}
*{box-sizing:border-box;margin:0;padding:0}
html,body{width:930px;height:1200px;overflow:hidden;background:var(--stage)}
body{position:relative;font-family:"Montserrat",Arial,sans-serif;color:var(--ink)}
.spread{position:absolute;left:103px;width:724px;height:467px;background:var(--paper);overflow:hidden}
.spread--outside{top:81px}
.spread--inside{top:632px}
.spread::after{content:"";position:absolute;left:0;right:0;bottom:0;height:3px;background:var(--green)}
.fold{position:absolute;left:362px;top:0;bottom:0;width:1px;background:#e2e2e2}
.abs{position:absolute}

/* outside: back cover */
.about{left:37px;top:0;width:164px;height:222px;background:var(--blue);color:var(--white);padding:0 22px 0 23px}
.about__title{margin-top:34px;font-family:"Poppins",sans-serif;font-weight:400;font-size:11.6px;padding-bottom:4px;border-bottom:1px solid rgba(255,255,255,.8)}
.about__title b{font-weight:700}
.about__text{margin-top:10px;font-size:5.6px;line-height:8.2px;font-weight:300}
.about__list{list-style:none;margin-top:9px}
.about__list li{display:flex;align-items:center;gap:5px;font-family:"Poppins",sans-serif;font-weight:500;font-size:8px;height:15px;border-bottom:1px solid rgba(255,255,255,.35)}
.experts{left:37px;top:222px;width:164px;height:74px;background:var(--green);color:var(--white);padding:16px 0 0 17px;font-family:"Poppins",sans-serif}
.experts__big{font-size:14.5px;font-weight:700;line-height:15px}
.experts__small{font-size:7.6px;font-weight:600;line-height:9px}
.experts__ask{font-size:7.6px;font-weight:600;margin-top:6px}
.contact-title{left:37px;top:331px;width:281px;font-family:"Poppins",sans-serif;font-size:11.6px;font-weight:400;padding-bottom:4px;border-bottom:1px solid var(--green)}
.contact-title b{color:var(--blue);font-weight:600}
.contact{left:37px;top:360px;font-family:"Poppins",sans-serif;font-size:8.4px;line-height:10px;font-weight:500}
.contact__row{display:flex;gap:5px;align-items:flex-start;margin-bottom:6px}
.contact__row svg{flex:none;margin-top:1px}
.socials{left:261px;top:377px;display:flex;gap:7px}
.socials span{width:14px;height:14px;border-radius:50%;background:var(--blue)}
.brand{display:flex;align-items:center;gap:5px;font-family:"Poppins",sans-serif;font-weight:700;color:var(--blue);white-space:nowrap}
.brand__dot{width:18px;height:18px;border-radius:50%;background:var(--green);flex:none}
.brand--back{left:196px;top:416px;font-size:9.6px}
.brand--front{left:536px;top:418px;font-size:10.6px}
.brand--front .brand__dot{width:22px;height:22px}

/* outside: front cover */
.lobby-photo{left:253px;top:0;width:471px;height:288px;background:
  linear-gradient(180deg,rgba(0,0,0,0) 55%,rgba(58,36,22,.55) 100%),
  linear-gradient(100deg,#5d3e25 0%,#a87a4e 22%,#e9e1d4 40%,#cfc4b6 52%,#7a5032 70%,#3a2a20 100%)}
.lobby-bar{left:253px;top:288px;width:471px;height:5px;background:var(--green)}
.tech-photo{left:540px;top:225px;width:152px;height:176px;background:linear-gradient(180deg,#fbfcfd 0%,#e8ecf1 70%,#d4dae2 100%);border-radius:48px 48px 0 0;z-index:1}
.cover-title{left:394px;top:328px;font-family:"Poppins",sans-serif;font-weight:600;font-size:16.5px;line-height:20.5px;z-index:2;white-space:nowrap}
.cover-title span{color:var(--blue)}
.cover-rule{left:394px;top:401px;width:298px;height:1px;background:var(--blue);z-index:2}
.cover-web{left:394px;top:431px;font-family:"Poppins",sans-serif;font-size:7.8px;letter-spacing:1.6px;font-weight:500}
.cover-web span{color:var(--blue)}

/* inside left */
.headline{font-family:"Poppins",sans-serif;font-weight:600;color:var(--green);font-size:24px;line-height:28px;white-space:nowrap}
.headline--left{left:35px;top:27px}
.banner{background:var(--blue);color:var(--white);font-family:"Poppins",sans-serif;font-weight:600;text-align:center;border-radius:4px 4px 0 0;white-space:nowrap}
.banner--answers{left:37px;top:59px;width:290px;height:23px;font-size:13.6px;line-height:23px;border-radius:3px}
.room-photo--big{left:37px;top:98px;width:184px;height:159px;background:
  radial-gradient(circle at 28% 68%,#b8423a 0 9%,transparent 10%),
  linear-gradient(90deg,#efe9e2 0%,#f6f2ee 45%,#5b4a44 58%,#eef1f4 70%,#dfe5ec 100%)}
.room-photo--top{left:225px;top:98px;width:100px;height:77px;background:linear-gradient(90deg,#dfe4ea 0%,#f4f6f8 45%,#ece6df 60%,#6e5546 100%)}
.room-photo--bottom{left:225px;top:180px;width:100px;height:77px;background:linear-gradient(90deg,#8f7c6c 0%,#c9bdb1 35%,#f1f2f4 55%,#d46a45 75%,#6d6157 100%)}
.section-rule{height:1px;background:var(--blue)}
.tab{background:var(--blue);color:var(--white);font-family:"Poppins",sans-serif;font-weight:600;font-size:14px;text-align:center;line-height:22px;clip-path:polygon(4% 0,100% 0,96% 100%,0 100%);white-space:nowrap}
.rule--work{left:30px;top:296px;width:303px}
.tab--work{left:101px;top:275px;width:164px;height:22px}
.step{top:307px;width:96px;text-align:center}
.step__icon{display:block;margin:0 auto}
.step__name{font-family:"Poppins",sans-serif;font-weight:600;color:var(--blue);font-size:10px;margin-top:8px;padding-bottom:3px;border-bottom:1px solid var(--green);margin-left:10px;margin-right:10px}
.step__text{font-size:6.2px;line-height:8.2px;color:var(--grey);margin-top:5px}

/* inside right */
.headline--right{left:420px;top:28px}
.banner--hotel{left:399px;top:59px;width:290px;height:24px;font-size:22px;line-height:26px}
.hotel-box{left:399px;top:83px;width:290px;height:156px;background:linear-gradient(90deg,#f2efea,#fbfaf8);border:1px solid #d8d8d8}
.hotel-tech{left:399px;top:83px;width:103px;height:156px;background:
  linear-gradient(180deg,#7a604b 0%,#8a6d57 30%,#e9ecef 45%,#f5f6f7 55%,#2f5fb8 68%,#21459a 100%)}
.pest{width:56px;text-align:center}
.pest__label{font-family:"Poppins",sans-serif;font-weight:500;font-size:5.8px;margin-top:3px;letter-spacing:.2px}
.rule--why{left:391px;top:276px;width:305px}
.tab--why{left:464px;top:255px;width:163px;height:22px}
.reason{top:289px;width:100px;text-align:center}
.reason__name{font-family:"Poppins",sans-serif;font-weight:600;color:var(--blue);font-size:7.4px;margin-top:6px}
.reason__text{font-size:5.3px;line-height:7px;color:var(--grey);margin-top:4px}
.closing{left:399px;top:405px;width:290px;font-size:5.1px;line-height:7px;color:var(--grey)}
</style>
</head>
<body>

<section class="spread spread--outside">
  <div class="fold"></div>

  <div class="abs about">
    <h2 class="about__title">ABOUT <b>US</b></h2>
    <p class="about__text">At Brindlewick Pest Control, our licensed technicians have extensive knowledge and experience in providing the best treatments and solutions to get rid of all those unwanted critters including:</p>
    <ul class="about__list">
      <li><svg width="7" height="7" viewBox="0 0 10 10"><circle cx="5" cy="5" r="4.3" fill="none" stroke="#fff"/><path d="M3 5.2l1.4 1.4L7 3.9" fill="none" stroke="#fff"/></svg>FLEAS</li>
      <li><svg width="7" height="7" viewBox="0 0 10 10"><circle cx="5" cy="5" r="4.3" fill="none" stroke="#fff"/><path d="M3 5.2l1.4 1.4L7 3.9" fill="none" stroke="#fff"/></svg>BED BUGS</li>
      <li><svg width="7" height="7" viewBox="0 0 10 10"><circle cx="5" cy="5" r="4.3" fill="none" stroke="#fff"/><path d="M3 5.2l1.4 1.4L7 3.9" fill="none" stroke="#fff"/></svg>RODENTS</li>
      <li><svg width="7" height="7" viewBox="0 0 10 10"><circle cx="5" cy="5" r="4.3" fill="none" stroke="#fff"/><path d="M3 5.2l1.4 1.4L7 3.9" fill="none" stroke="#fff"/></svg>PEST CONTROL</li>
      <li><svg width="7" height="7" viewBox="0 0 10 10"><circle cx="5" cy="5" r="4.3" fill="none" stroke="#fff"/><path d="M3 5.2l1.4 1.4L7 3.9" fill="none" stroke="#fff"/></svg>AND MUCH MORE</li>
    </ul>
  </div>

  <div class="abs experts">
    <p class="experts__big">OUR EXPERTS</p>
    <p class="experts__small">WILL SOLVE THEM IN NO TIME.</p>
    <p class="experts__ask">Have Any Pest Problems?</p>
  </div>

  <h2 class="abs contact-title">CONTACT <b>INFO</b></h2>
  <div class="abs contact">
    <div class="contact__row">
      <svg width="6" height="8" viewBox="0 0 6 8"><path d="M3 7.6S.4 4.6.4 2.9a2.6 2.6 0 015.2 0C5.6 4.6 3 7.6 3 7.6z" fill="none" stroke="#0b66bf" stroke-width=".8"/><circle cx="3" cy="2.9" r=".9" fill="#0b66bf"/></svg>
      <div>2840 Harbor Ridge Road<br>#310<br>Lakeport, CA 95453</div>
    </div>
    <div class="contact__row">
      <svg width="6" height="7" viewBox="0 0 10 10"><path d="M2 1l2 2-1 1.5c.8 1.4 1.6 2.2 3 3L7.5 6.5l2 2L8 10C4 9.5.5 6 0 2z" fill="#0b66bf"/></svg>
      <div>555-014-2290</div>
    </div>
    <div class="contact__row">
      <svg width="6" height="7" viewBox="0 0 10 10"><rect x=".5" y="1.5" width="9" height="8" fill="none" stroke="#0b66bf"/><path d="M.5 4h9" stroke="#0b66bf"/></svg>
      <div>Mon-Fri: 9:00am-5:00pm</div>
    </div>
    <div class="contact__row">
      <svg width="7" height="7" viewBox="0 0 10 10"><circle cx="5" cy="5" r="4.4" fill="none" stroke="#0b66bf" stroke-width=".9"/><ellipse cx="5" cy="5" rx="2" ry="4.4" fill="none" stroke="#0b66bf" stroke-width=".8"/><path d="M.6 5h8.8" stroke="#0b66bf" stroke-width=".8"/></svg>
      <div>www.getbrindlewick.com</div>
    </div>
  </div>
  <div class="abs socials"><span></span><span></span><span></span></div>
  <div class="abs brand brand--back"><span class="brand__dot"></span>BRINDLEWICK PEST CONTROL</div>

  <div class="abs lobby-photo" role="img" aria-label="Hotel lobby: guests at the marble reception desk with masked staff"></div>
  <div class="abs lobby-bar"></div>
  <div class="abs tech-photo" role="img" aria-label="Technician in white protective suit holding a sprayer"></div>

  <h1 class="abs cover-title">The Smarter<br>Approach<br>To <span>Pest Control</span></h1>
  <div class="abs cover-rule"></div>
  <p class="abs cover-web">www.<span>getbrindlewick</span>.com</p>
  <div class="abs brand brand--front"><span class="brand__dot"></span>BRINDLEWICK PEST CONTROL</div>
</section>

<section class="spread spread--inside">
  <div class="fold"></div>

  <h2 class="abs headline headline--left">You have pest problems,</h2>
  <div class="abs banner banner--answers">Brindlewick Pest Control has answers</div>
  <div class="abs room-photo--big" role="img" aria-label="Technician disinfecting a hotel bedroom"></div>
  <div class="abs room-photo--top" role="img" aria-label="Technician spraying a hotel doorway"></div>
  <div class="abs room-photo--bottom" role="img" aria-label="Technician treating a hotel corridor"></div>

  <div class="abs section-rule rule--work"></div>
  <div class="abs tab tab--work">WORK PRINCIPLE</div>

  <div class="abs step" style="left:20px">
    <svg class="step__icon" width="66" height="66" viewBox="0 0 66 66"><circle cx="33" cy="33" r="31.5" fill="#fff" stroke="#6cc24a" stroke-width="1.2"/><rect x="22" y="16" width="22" height="30" fill="none" stroke="#999" stroke-width="1"/><g stroke="#6cc24a" stroke-width="1.2" fill="none"><path d="M25 23l1.5 1.5 2.5-3M25 30l1.5 1.5 2.5-3M25 37l1.5 1.5 2.5-3"/></g><path d="M31 23h10M31 30h10M31 37h10" stroke="#999"/><circle cx="33" cy="56" r="5" fill="#6cc24a"/><text x="33" y="58.3" font-size="6.5" fill="#fff" text-anchor="middle" font-family="Poppins,sans-serif">1</text></svg>
    <p class="step__name">INSPECTION</p>
    <p class="step__text">Our technicians will do a thorough inspection of the area to locate where your pests are hiding and seeking shelter.</p>
  </div>
  <div class="abs step" style="left:133px">
    <svg class="step__icon" width="66" height="66" viewBox="0 0 66 66"><circle cx="33" cy="33" r="31.5" fill="#fff" stroke="#6cc24a" stroke-width="1.2"/><rect x="26" y="22" width="12" height="22" rx="2" fill="none" stroke="#999"/><path d="M29 22v-5h6v5M38 26l9 14" stroke="#999" fill="none"/><path d="M43 20l6 12" stroke="#6cc24a" stroke-width="2"/><circle cx="33" cy="56" r="5" fill="#6cc24a"/><text x="33" y="58.3" font-size="6.5" fill="#fff" text-anchor="middle" font-family="Poppins,sans-serif">2</text></svg>
    <p class="step__name">DISINFECTION</p>
    <p class="step__text">We spray the affected area using the latest chemical and treatment solution so bugs and insects are killed instantly.</p>
  </div>
  <div class="abs step" style="left:247px">
    <svg class="step__icon" width="66" height="66" viewBox="0 0 66 66"><circle cx="33" cy="33" r="31.5" fill="#fff" stroke="#6cc24a" stroke-width="1.2"/><path d="M19 32l14-12 14 12M23 29v16h20V29" fill="none" stroke="#999"/><rect x="29" y="35" width="8" height="10" fill="none" stroke="#999"/><path d="M22 14v6M19 17h6M44 20v8M40 24h8" stroke="#6cc24a" stroke-width="1.2"/><circle cx="33" cy="56" r="5" fill="#6cc24a"/><text x="33" y="58.3" font-size="6.5" fill="#fff" text-anchor="middle" font-family="Poppins,sans-serif">3</text></svg>
    <p class="step__name">PREVENTION</p>
    <p class="step__text">Schedule a monthly, bi monthly, quarterly or yearly service with us to ensure pests are gone for good.</p>
  </div>

  <h2 class="abs headline headline--right">How Can We Protect</h2>
  <div class="abs banner banner--hotel">Your Hotel?</div>
  <div class="abs hotel-box"></div>
  <div class="abs hotel-tech" role="img" aria-label="Technician in hard hat and blue overalls with a sprayer"></div>

  <div class="abs pest" style="left:513px;top:90px"><svg width="28" height="28" viewBox="0 0 28 28"><circle cx="14" cy="14" r="12.5" fill="#e7c9b3" stroke="#0b66bf" stroke-width="2"/><path d="M5 5l18 18" stroke="#0b66bf" stroke-width="2"/></svg><p class="pest__label">COCKROACHES</p></div>
  <div class="abs pest" style="left:571px;top:90px"><svg width="28" height="28" viewBox="0 0 28 28"><circle cx="14" cy="14" r="12.5" fill="#e8b98f" stroke="#0b66bf" stroke-width="2"/><path d="M5 5l18 18" stroke="#0b66bf" stroke-width="2"/></svg><p class="pest__label">FLEAS</p></div>
  <div class="abs pest" style="left:627px;top:90px"><svg width="28" height="28" viewBox="0 0 28 28"><circle cx="14" cy="14" r="12.5" fill="#e9d3c6" stroke="#0b66bf" stroke-width="2"/><path d="M5 5l18 18" stroke="#0b66bf" stroke-width="2"/></svg><p class="pest__label">ANTS</p></div>
  <div class="abs pest" style="left:513px;top:138px"><svg width="28" height="28" viewBox="0 0 28 28"><circle cx="14" cy="14" r="12.5" fill="#e4e2df" stroke="#0b66bf" stroke-width="2"/><path d="M5 5l18 18" stroke="#0b66bf" stroke-width="2"/></svg><p class="pest__label">MOSQUITOES</p></div>
  <div class="abs pest" style="left:571px;top:138px"><svg width="28" height="28" viewBox="0 0 28 28"><circle cx="14" cy="14" r="12.5" fill="#d9b478" stroke="#0b66bf" stroke-width="2"/><path d="M5 5l18 18" stroke="#0b66bf" stroke-width="2"/></svg><p class="pest__label">WASPS</p></div>
  <div class="abs pest" style="left:627px;top:138px"><svg width="28" height="28" viewBox="0 0 28 28"><circle cx="14" cy="14" r="12.5" fill="#b59a88" stroke="#0b66bf" stroke-width="2"/><path d="M5 5l18 18" stroke="#0b66bf" stroke-width="2"/></svg><p class="pest__label">SPIDERS</p></div>
  <div class="abs pest" style="left:513px;top:186px"><svg width="28" height="28" viewBox="0 0 28 28"><circle cx="14" cy="14" r="12.5" fill="#d6d1cc" stroke="#0b66bf" stroke-width="2"/><path d="M5 5l18 18" stroke="#0b66bf" stroke-width="2"/></svg><p class="pest__label">RODENTS</p></div>
  <div class="abs pest" style="left:571px;top:186px"><svg width="28" height="28" viewBox="0 0 28 28"><circle cx="14" cy="14" r="12.5" fill="#e2a06a" stroke="#0b66bf" stroke-width="2"/><path d="M5 5l18 18" stroke="#0b66bf" stroke-width="2"/></svg><p class="pest__label">BED BUGS</p></div>
  <div class="abs pest" style="left:627px;top:186px"><svg width="28" height="28" viewBox="0 0 28 28"><circle cx="14" cy="14" r="12.5" fill="#c9828a" stroke="#0b66bf" stroke-width="2"/><path d="M5 5l18 18" stroke="#0b66bf" stroke-width="2"/></svg><p class="pest__label">COVID-19</p></div>

  <div class="abs section-rule rule--why"></div>
  <div class="abs tab tab--why">WHY CHOOSE US</div>

  <div class="abs reason" style="left:395px">
    <svg width="30" height="22" viewBox="0 0 30 22"><rect x="1" y="1" width="28" height="20" fill="none" stroke="#6cc24a"/><circle cx="10" cy="10" r="5" fill="none" stroke="#6cc24a"/><path d="M8 15l-1 5 3-2 3 2-1-5M18 8h8M18 12h8" stroke="#6cc24a" fill="none"/></svg>
    <p class="reason__name">Elite Technicians</p>
    <p class="reason__text">Our technicians are highly trained and qualified to recognize a variety of pests invading your commercial or residential property. They are up to date with the latest technology and available products so you can rest assure you receive the best treatment.</p>
  </div>
  <div class="abs reason" style="left:507px">
    <svg width="30" height="22" viewBox="0 0 30 22"><path d="M3 10h5v11H3zM8 11l5-8c2 0 2 2 1.5 4H19c1.5 0 2 1.5 1.5 3l-2 7c-.3 1-1 1.5-2 1.5H8" fill="none" stroke="#6cc24a"/><path d="M22 3h6v10h-6z" fill="none" stroke="#6cc24a"/></svg>
    <p class="reason__name">Great Prices</p>
    <p class="reason__text">When it comes to getting rid of those unwanted critters, our prices are unbeatable. Our rates are competitive so you can be at ease knowing our prices will fit into your range.</p>
  </div>
  <div class="abs reason" style="left:605px">
    <svg width="30" height="22" viewBox="0 0 30 22"><circle cx="15" cy="5" r="3.5" fill="none" stroke="#6cc24a"/><circle cx="6" cy="9" r="3" fill="none" stroke="#6cc24a"/><circle cx="24" cy="9" r="3" fill="none" stroke="#6cc24a"/><path d="M15 9v12M6 12v8M24 12v8M6 16h18" stroke="#6cc24a" fill="none"/></svg>
    <p class="reason__name">Variety of Services</p>
    <p class="reason__text">From the smallest animal like a termite to a slithering snake, we offer many different services so you can consider your one stop shop when it comes to termite and pest control.</p>
  </div>

  <p class="abs closing">Count on the professionals at Brindlewick Pest Control to handle your pests problems throughout the seasons. We are an established and trusted pest control company and our mission is to keep pests off your property, guaranteed! We will do whatever it takes to make sure your home and business are protected and your pest problems are behind you. When you contact us for services, you can rest assured knowing that we will do whatever it takes to make sure your pest problems are eliminated. No one wants to find a spider or rat inside their building because of the damage they can cause. You can rely on us for all your commercial and residential pest problems.</p>
</section>

</body>
</html>
```